Candle company needs a label for candle

Looking for a designer to create my candle label. I am going to attach a few pictures of my vision for the label as well as my Company Logo and jar I have puchased. I'm going for the modern rustic feel but you are the designer and have full trust in your abilities. The label is going to be printed on Kraft paper (2x3) so looking for the font to be black. The candle label MUST include the following information:
Candle Birchway Co.
NO. 01: Eucalyptus + Spearmint
Handmade In NJ
Soy Wax
9oz

Industry/Entity Type

Candle Industry

Colors

Designer to choose colors to be used in the design.

Requirements
Should not have
• Any images

```html
<!DOCTYPE html>
<html lang="en">
<head>
<meta charset="utf-8">
<title>Candle Birchway Co. — No 01 Label</title>
<link href="https://fonts.googleapis.com/css2?family=Cormorant+Garamond:ital,wght@0,500;0,600;1,500&family=Cormorant+SC:wght@500;600&display=swap" rel="stylesheet">
<style>
  :root {
    --page: #ffffff;
    --paper: #ecebe8;
    --paper-shade: #e2e1dd;
    --ink: #2f3133;
    --sage: #798a63;
    --rule: #6d6f70;
  }
  * { margin: 0; padding: 0; box-sizing: border-box; }
  html, body { width: 1200px; height: 1002px; overflow: hidden; background: var(--page); }
  .canvas { position: relative; width: 1200px; height: 1002px; }

  .label {
    position: absolute; left: 320px; top: 80px;
    width: 560px; height: 842px;
    background: linear-gradient(160deg, var(--paper) 0%, var(--paper-shade) 100%);
    color: var(--ink);
    font-family: "Cormorant Garamond", serif;
    font-variant-numeric: lining-nums;
  }

  .brand-name {
    position: absolute; left: 52px; top: 250px; width: 457px;
    text-align: center; white-space: nowrap;
    font-family: "Cormorant Garamond", serif;
    font-weight: 500; font-size: 46px; line-height: 56px;
    color: var(--ink);
  }

  .number {
    position: absolute; left: 0; width: 100%; top: 452px;
    text-align: center; color: var(--sage);
    font-family: "Cormorant Garamond", serif; font-weight: 600;
    font-size: 58px; line-height: 64px; letter-spacing: -0.02em;
    font-variant-numeric: lining-nums;
  }

  .rule { position: absolute; left: 52px; width: 457px; border-top: 1.5px dotted var(--rule); }
  .rule.r1 { top: 532px; } .rule.r2 { top: 539px; }
  .rule.r3 { top: 609px; } .rule.r4 { top: 616px; }
  .rule.r5 { top: 690px; } .rule.r6 { top: 780px; }
  .divider { position: absolute; left: 282px; top: 692px; height: 88px; border-left: 1.5px dotted var(--rule); }

  .scent, .origin {
    position: absolute; left: 52px; width: 457px; text-align: center;
    font-family: "Cormorant SC", serif; white-space: nowrap;
  }
  .scent { top: 555px; font-size: 34px; line-height: 40px; letter-spacing: 0.05em; font-weight: 600; }
  .origin { top: 634px; font-size: 30px; line-height: 40px; letter-spacing: 0.22em; font-weight: 500; }

  .spec { position: absolute; top: 713px; font-size: 32px; line-height: 44px; text-align: center; font-variant-numeric: lining-nums; }
  .spec.wax { left: 52px; width: 230px; font-style: italic; }
  .spec.weight { left: 282px; width: 227px; }
</style>
</head>
<body>
<main class="canvas">
  <section class="label">
    <p class="brand-name">Candle Birchway Co.</p>

    <p class="number">N° 01:</p>

    <div class="rule r1"></div><div class="rule r2"></div>
    <p class="scent">Eucalyptus &amp; Spearmint</p>
    <div class="rule r3"></div><div class="rule r4"></div>
    <p class="origin">Handmade In NJ</p>
    <div class="rule r5"></div>
    <p class="spec wax">Soy Wax</p>
    <div class="divider"></div>
    <p class="spec weight">9oz</p>
    <div class="rule r6"></div>
  </section>
</main>
</body>
</html>
```